Custom Graphic Design For Online Shopping Service Homepage

We need a graphic design for the homepage of our company website. This is the 1st image for the slideshow module on the homepage that will require only 1 graphic with a continuous background for the other slideshows. So a psd file with the background image and content image.
This is a multi-part project and selected individual(s) will be invited to participate in next assignments for future web/graphic designs.

Our company is called 'BuyNorthway.com' where we provide an online personal shopping service where we shop for customers and provide quality service. The central theme should be to get the cheapest prices online while getting the best in-store type shopping experience.

The design chosen will be something that has a unique style and represents our company logo the best.
The main focus will be to have the image represent the "future of online shopping" with a personalized touch and lesson. Something friendly but not just random people smiling at you that make you think we're selling products.
Some ideas for the image would be like an internet shopping concept, a shopping mall that's help you shop, a professional shopper equates to saving time and money.
http://www.layoutfoundry.example/demo/58214.html
This is more of the content and background matching for the slideshow. A current screenshot of the site is shown with the black area the requirements.
Updates

Project Deadline Extended
Reason: allow for more time to design image due to change

The menu top has changed to an interactive tidal menu with the logo on the top left corner.
http://demo.brightaddons.example/tidal-menu.html

I wouldn't worry too much about matching font colors for the background, i just need the proper background color to match the menu and slideshow content.  A lighter color seems to fit the style better.  I have attached a preview of what I need in the black.  Please ignore extra content from the page since a web design is not needed but a content design for the slideshow.

The payment is now guaranteed and I have upped the first place prize $20 to $200 for extending the job.

A better example would be this slideshow with the content matching background.
We apologize for the requirements for the design.

Target Market(s)

Online shoppers that don't have time to shop, people who want to save money, less tech-savy shoppers

Industry/Entity Type

Graphic Design

Requirements
Must have
• 1 continuous background in slideshow and 1 content image inside
The background is very important because it will be used for the next 3 images.
http://www.velmore.example/ - This is the size background we want, not exactly the style and color though.
http://www.quillguard.example/
Nice to have
• We have a logo but it does not need to be displayed into the graphic(optional). Could be good as a reference but the logo for now will be next to the menu on the top left like the velmore design.
Should not have
• Buttons and menus, they will be added for the web design project.

```html
<!DOCTYPE html>
<html lang="en">
<head>
<meta charset="utf-8">
<title>BuyNorthway.com — Online Personal Shopping</title>
<link rel="stylesheet" href="https://fonts.googleapis.com/css2?family=Arimo:wght@400;700&family=Maven+Pro:wght@400;500;700&family=Open+Sans:wght@300;400&family=Ubuntu:wght@500;700&display=swap">
<style>
  :root {
    --header-bg: #e8e8e8;
    --page-bg: #ffffff;
    --ink-dark: #123c4c;
    --ink-body: #333333;
    --ink-muted: #555555;
    --icon-grey: #a8a8a8;
    --nav-green: #6a9a1c;
    --nav-orange: #f08a18;
    --nav-red: #8a1e1e;
    --nav-teal: #3aaec0;
    --nav-purple: #4d4a86;
    --nav-maroon: #8e1c1c;
    --logo-ink: #f07a12;
    --button-blue: #1a8fe2;
    --arrow-bg: #4a3a1c;
    --rule: #dcdcdc;
  }
  * { margin: 0; padding: 0; box-sizing: border-box; }
  html, body { width: 1200px; height: 670px; overflow: hidden; background: var(--page-bg); }
  body { position: relative; font-family: "Arimo", Arial, sans-serif; color: var(--ink-body); }

  .site-header { position: absolute; left: 0; top: 0; width: 1200px; height: 102px; background: var(--header-bg); }
  .brand { position: absolute; left: 258px; top: 46px; display: flex; align-items: center; gap: 8px; }
  .brand-mark { width: 14px; height: 14px; border-radius: 50%; background: var(--logo-ink); }
  .brand-name { font-family: "Ubuntu", sans-serif; font-weight: 700; font-size: 24px; color: var(--logo-ink); letter-spacing: -0.3px; }

  .main-nav { position: absolute; left: 0; top: 0; }
  .nav-item { position: absolute; top: 64px; width: 76px; text-align: center; font-family: "Ubuntu", sans-serif; font-weight: 700; font-size: 11.5px; }
  .nav-tab { position: absolute; top: 90px; width: 76px; height: 14px; border: 2px solid #fff; border-bottom: none; border-radius: 6px 6px 0 0; box-shadow: 0 0 3px rgba(0,0,0,.25); }

  .hero { position: absolute; left: 0; top: 102px; width: 1200px; height: 349px; overflow: hidden;
    background:
      radial-gradient(ellipse 380px 260px at 560px 40px, rgba(200,40,0,.55), transparent 70%),
      radial-gradient(ellipse 300px 220px at 760px 330px, rgba(240,230,20,.8), transparent 70%),
      radial-gradient(ellipse 260px 200px at 1150px 280px, rgba(60,150,210,.6), transparent 70%),
      linear-gradient(90deg, #ff6a10 0%, #ff8a10 35%, #ffb818 55%, #d8e020 75%, #90d830 90%, #8acc60 100%);
  }
  .hero-title { position: absolute; left: 203px; top: 38px; font-family: "Open Sans", sans-serif; font-weight: 300; font-size: 37px; line-height: 43px; color: #fff; }
  .hero-text { position: absolute; left: 203px; top: 140px; width: 300px; font-size: 10.4px; line-height: 19px; color: #5a2a0a; }
  .hero-button { position: absolute; left: 203px; top: 216px; width: 138px; height: 36px; background: var(--button-blue); border-radius: 3px; color: #fff; font-family: "Ubuntu", sans-serif; font-weight: 500; font-size: 14px; line-height: 36px; text-align: center; box-shadow: 0 2px 3px rgba(0,0,0,.2); }
  .hero-dots { position: absolute; left: 205px; top: 284px; display: flex; gap: 10px; }
  .hero-dots span { width: 10px; height: 10px; border-radius: 50%; background: #fff; }
  .hero-dots span.is-active { background: #333; }
  .hero-arrow { position: absolute; top: 144px; width: 26px; height: 26px; background: var(--arrow-bg); opacity: .85; }
  .hero-arrow svg { display: block; }
  .hero-photo { position: absolute; left: 550px; top: 44px; width: 369px; height: 247px; border: 2px solid #fff;
    background: linear-gradient(135deg, #dfe8f0 0%, #c8d6e2 45%, #9fb4c4 75%, #e8eef2 100%); }
  .hero-shadow { position: absolute; left: 570px; top: 293px; width: 330px; height: 22px; border-radius: 50%; background: radial-gradient(ellipse, rgba(90,90,0,.35), transparent 70%); }

  .tagline-band { position: absolute; left: 72px; top: 451px; width: 1056px; height: 80px; background: linear-gradient(180deg, #eef8fa, #ffffff); }
  .tagline { position: absolute; left: 216px; top: 472px; width: 752px; text-align: center; font-family: "Maven Pro", sans-serif; font-weight: 500; font-size: 16px; letter-spacing: .4px; color: var(--ink-dark); }
  .tagline-rule { position: absolute; left: 216px; top: 513px; width: 752px; height: 2px; background: var(--rule); }

  .feature { position: absolute; width: 240px; }
  .feature h3 { font-family: "Maven Pro", sans-serif; font-weight: 400; font-size: 15.5px; color: var(--ink-dark); letter-spacing: .2px; }
  .feature p { position: absolute; left: 38px; top: 28px; width: 200px; font-size: 9.6px; line-height: 16.5px; color: var(--ink-body); }
  .feature svg { position: absolute; left: 0; top: 30px; }
</style>
</head>
<body>
  <header class="site-header">
    <div class="brand"><span class="brand-mark"></span><span class="brand-name">BuyNorthway.com</span></div>
    <nav class="main-nav">
      <span class="nav-item" style="left:477px;color:var(--nav-green)">ABOUT US</span>
      <span class="nav-item" style="left:565px;color:var(--nav-orange)">FEATURES</span>
      <span class="nav-item" style="left:653px;color:var(--nav-red)">PRICES</span>
      <span class="nav-item" style="left:741px;color:var(--nav-teal)">BLOG</span>
      <span class="nav-item" style="left:829px;color:var(--nav-purple)">CONTACT US</span>
      <span class="nav-item" style="left:917px;color:var(--nav-maroon)">MEMBERS</span>
      <span class="nav-tab" style="left:479px;background:var(--nav-green)"></span>
      <span class="nav-tab" style="left:567px;background:var(--nav-orange)"></span>
      <span class="nav-tab" style="left:655px;background:var(--nav-red)"></span>
      <span class="nav-tab" style="left:743px;background:var(--nav-teal)"></span>
      <span class="nav-tab" style="left:831px;background:var(--nav-purple)"></span>
      <span class="nav-tab" style="left:919px;background:var(--nav-maroon)"></span>
    </nav>
  </header>

  <section class="hero">
    <h1 class="hero-title">An online personal<br>shopping service</h1>
    <p class="hero-text">We shop for customers and provide quality service. The central theme should be to get the cheapest prices online while getting the best in-store type shopping experience.</p>
    <a class="hero-button">Find out more</a>
    <div class="hero-dots"><span class="is-active"></span><span></span><span></span></div>
    <div class="hero-arrow" style="left:154px">
      <svg width="26" height="26" viewBox="0 0 26 26"><path d="M15 8 L10 13 L15 18" fill="none" stroke="#fff" stroke-width="2.5"/></svg>
    </div>
    <div class="hero-arrow" style="left:957px">
      <svg width="26" height="26" viewBox="0 0 26 26"><path d="M11 8 L16 13 L11 18" fill="none" stroke="#fff" stroke-width="2.5"/></svg>
    </div>
    <div class="hero-photo" role="img" aria-label="Photo of a hand holding a credit card and tapping a tablet screen"></div>
    <div class="hero-shadow"></div>
  </section>

  <div class="tagline-band"></div>
  <h2 class="tagline">FUNCTIONAL AND AWESOME KESTREL, PAGECRAFT AND HTML TEMPLATES FOR EVERYONE.</h2>
  <div class="tagline-rule"></div>

  <article class="feature" style="left:216px;top:542px">
    <h3>960 GRID SYSTEM</h3>
    <svg width="28" height="28" viewBox="0 0 28 28" fill="var(--icon-grey)"><rect x="0" y="0" width="26" height="3"/><rect x="0" y="6" width="18" height="3"/><rect x="0" y="12" width="26" height="3"/><circle cx="2" cy="21" r="1.5"/><circle cx="8" cy="21" r="1.5"/><circle cx="14" cy="21" r="1.5"/></svg>
    <p>Our templates use the popular gridframe css framework which makes developing much easier and enjoying.</p>
  </article>
  <article class="feature" style="left:472px;top:542px">
    <h3>COST EFFECTIVE</h3>
    <svg width="28" height="28" viewBox="0 0 28 28"><path d="M0 2 L0 10 L15 25 L25 15 L10 0 L2 0 Z" fill="var(--icon-grey)"/><circle cx="5" cy="5" r="2" fill="#fff"/></svg>
    <p>These templates are truly some great deals! They include so many features for a relatively small amount of money.</p>
  </article>
  <article class="feature" style="left:728px;top:542px">
    <h3>TECHNICAL SUPPORT</h3>
    <svg width="28" height="28" viewBox="0 0 28 28" fill="none" stroke="var(--icon-grey)" stroke-width="3"><rect x="2" y="2" width="15" height="11" rx="5"/><rect x="9" y="12" width="15" height="11" rx="5"/></svg>
    <p>Problems? Don't worry!! One of the biggest advantage of our templates is the technical support system. Let us know!</p>
  </article>

  <article class="feature" style="left:216px;top:646px"><h3>TIME SAVING</h3></article>
  <article class="feature" style="left:472px;top:646px"><h3>BROWSER COMPATIBILITY</h3></article>
  <article class="feature" style="left:728px;top:646px"><h3>MOBILE FRIENDLY</h3></article>
</body>
</html>
```